Cork And Lantern Email Template for Specials and Events

We need a professional looking template that we can use in mailchimp to communicate via email with our customers. Template needs to look clean and concise to drive sales to our website and store. We want a place to post a couple specials and another area to higlight upcoming events. We would also may like and area to tell whats hot. We are open to ideas just need a process that we can drop our products and events in and drive business.

Target Market(s)

Our Email customer base. They are all past customers who have purchased Craft Beer, Wine, or Whiskey from us

Industry/Entity Type

Events

Requirements
Must have
• Place to highlight specials, and upcoming tasting events.
Nice to have
• Place to put interesting facts

```html
<!DOCTYPE html>
<html lang="en">
<head>
<meta charset="utf-8">
<title>Cork And Lantern – Specials &amp; Events Email</title>
<link href="https://fonts.googleapis.com/css2?family=Arimo:wght@400;700&family=Great+Vibes&display=swap" rel="stylesheet">
<style>
  :root {
    --wood-dark: #1c1c1e;
    --wood-mid: #2e2d2f;
    --black: #000000;
    --gold: #e9a63c;
    --gold-light: #f7d98a;
    --gold-deep: #b97a22;
    --maroon: #4a0000;
    --maroon-deep: #2a0000;
    --white: #ffffff;
    --photo-amber: #8a5a1c;
    --photo-brown: #3a2410;
    --photo-cream: #c9b79a;
  }
  * { margin: 0; padding: 0; box-sizing: border-box; }
  html, body { width: 1200px; height: 2256px; overflow: hidden; background: var(--black); }
  .email {
    position: relative; width: 1200px; height: 2256px; overflow: hidden;
    background: var(--black); font-family: 'Arimo', Arial, sans-serif; color: var(--white);
  }
  .abs { position: absolute; }

  /* header */
  .header-wood {
    left: 0; top: 0; width: 1200px; height: 470px;
    background: repeating-linear-gradient(180deg, var(--wood-dark) 0 9px, var(--wood-mid) 9px 12px, var(--wood-dark) 12px 22px);
  }
  .header-rule { left: 0; top: 466px; width: 1200px; height: 22px; background: linear-gradient(180deg, var(--gold-light), var(--gold) 40%, var(--gold-deep)); }
  .section-tag {
    border: 4px solid var(--white); background: var(--black);
    font-family: 'Great Vibes', cursive; color: var(--white);
    display: flex; align-items: center; justify-content: center; line-height: 1;
  }
  .tag-featured { left: -6px; top: 33px; width: 585px; height: 115px; font-size: 78px; }
  .tag-events { left: 644px; top: 621px; width: 570px; height: 116px; font-size: 76px; }

  .brand-badge {
    left: 688px; top: -8px; width: 550px; height: 570px; border-radius: 50%;
    border: 12px solid var(--gold);
    background: radial-gradient(circle at 45% 40%, var(--photo-amber), var(--photo-brown) 55%, #120a04);
    display: flex; align-items: center; justify-content: flex-start; padding-left: 50px;
  }
  .brand-name {
    font-family: 'Arimo', Arial, sans-serif; font-weight: 400; color: var(--white);
    font-size: 56px; line-height: 1.05; display: flex; align-items: center; gap: 18px;
  }
  .brand-dot { width: 30px; height: 30px; border-radius: 50%; background: var(--white); flex: none; }

  /* events band */
  .events-band { left: 0; top: 488px; width: 1200px; height: 400px; background: var(--black); }
  .pour-photo {
    left: 0; top: 488px; width: 640px; height: 400px;
    background: radial-gradient(ellipse at 35% 55%, #5a0a0e 0%, #24060a 30%, var(--black) 65%);
  }

  .ornament { left: 0; width: 1200px; }
  .thin-rule { height: 3px; background: linear-gradient(90deg, var(--gold-deep), var(--gold-light), var(--gold-deep)); }

  /* deals */
  .deals-photo {
    left: 18px; top: 978px; width: 1162px; height: 556px; border: 2px solid #777;
    background: linear-gradient(100deg, #2a1a0e 0%, var(--photo-cream) 22%, #4a3018 38%, #e8e2d6 50%, #3b2a18 62%, var(--photo-cream) 78%, #24160c 100%);
  }
  .deals-tag {
    left: 716px; top: 1033px; width: 427px; height: 441px;
    border: 3px solid #d9d9d9; outline: 3px solid #d9d9d9; outline-offset: 8px;
    display: flex; flex-direction: column; align-items: center; justify-content: center;
    font-weight: 700; font-size: 88px; line-height: 1.02; text-align: center; color: var(--white);
    background: rgba(0,0,0,0.05);
  }

  /* coupon */
  .coupon-text {
    left: 0; top: 1780px; width: 1200px; text-align: center;
    font-family: 'Great Vibes', cursive; font-size: 118px; color: var(--white); line-height: 1;
  }

  /* footer */
  .footer-wood {
    left: 0; top: 2060px; width: 1200px; height: 196px;
    background: repeating-linear-gradient(180deg, var(--wood-dark) 0 9px, var(--wood-mid) 9px 12px, var(--wood-dark) 12px 22px);
  }
  .footer-url { left: 20px; top: 2146px; font-size: 40px; color: var(--white); }
  .footer-brand { left: 860px; top: 2110px; }
  .footer-brand .brand-name { font-size: 46px; gap: 14px; }
  .footer-brand .brand-dot { width: 24px; height: 24px; }
</style>
</head>
<body>
<div class="email">

  <!-- header -->
  <div class="abs header-wood"></div>
  <div class="abs header-rule"></div>
  <div class="abs section-tag tag-featured">Featured Deals</div>

  <!-- events -->
  <div class="abs events-band"></div>
  <div class="abs pour-photo" role="img" aria-label="Red wine being poured into a glass against a dark background"></div>
  <div class="abs section-tag tag-events">Up Coming Events</div>

  <div class="abs brand-badge" role="img" aria-label="Wine bottles resting in a cellar rack, with the store name">
    <div class="brand-name"><span class="brand-dot"></span><span>Cork And<br>Lantern</span></div>
  </div>

  <svg class="abs ornament" style="top:810px" width="1200" height="130" viewBox="0 0 1200 130">
    <defs>
      <linearGradient id="goldStroke" x1="0" x2="1" y1="0" y2="0">
        <stop offset="0" stop-color="#b97a22"/><stop offset="0.5" stop-color="#f7d98a"/><stop offset="1" stop-color="#d59a35"/>
      </linearGradient>
    </defs>
    <path d="M0 92 H500 C555 92 585 55 600 12 C615 55 645 92 700 92 H1200" fill="none" stroke="url(#goldStroke)" stroke-width="18"/>
  </svg>
  <div class="abs thin-rule" style="left:40px; top:948px; width:430px;"></div>
  <div class="abs thin-rule" style="left:730px; top:948px; width:430px;"></div>

  <!-- saving deals -->
  <div class="abs deals-photo" role="img" aria-label="Wine bottles nestled in straw inside wooden crates"></div>
  <div class="abs deals-tag"><span>SAVING</span><span>DEALS</span></div>

  <!-- coupon area -->
  <svg class="abs ornament" style="top:1555px" width="1200" height="520" viewBox="0 0 1200 520">
    <defs>
      <linearGradient id="goldStroke2" x1="0" x2="1" y1="0" y2="0">
        <stop offset="0" stop-color="#b97a22"/><stop offset="0.5" stop-color="#f7d98a"/><stop offset="1" stop-color="#d59a35"/>
      </linearGradient>
      <linearGradient id="maroonFill" x1="0" x2="0" y1="0" y2="1">
        <stop offset="0" stop-color="#4a0000"/><stop offset="1" stop-color="#2a0000"/>
      </linearGradient>
    </defs>
    <path d="M0 62 H500 C555 62 585 35 600 8 C615 35 645 62 700 62 H1200 V498 H700 C645 498 615 520 600 550 C585 520 555 498 500 498 H0 Z" fill="url(#maroonFill)"/>
    <path d="M0 62 H500 C555 62 585 35 600 8 C615 35 645 62 700 62 H1200" fill="none" stroke="url(#goldStroke2)" stroke-width="18"/>
    <path d="M0 498 H500 C555 498 585 520 600 548" fill="none" stroke="url(#goldStroke2)" stroke-width="18"/>
    <path d="M600 548 C615 520 645 498 700 498 H1200" fill="none" stroke="url(#goldStroke2)" stroke-width="18"/>
  </svg>
  <div class="abs thin-rule" style="left:0; top:1670px; width:480px;"></div>
  <div class="abs thin-rule" style="left:720px; top:1670px; width:480px;"></div>
  <div class="abs coupon-text">Coupon Placement</div>
  <div class="abs thin-rule" style="left:0; top:2010px; width:500px;"></div>
  <div class="abs thin-rule" style="left:720px; top:2010px; width:480px;"></div>

  <!-- footer -->
  <div class="abs footer-wood" style="top:2095px; height:161px;"></div>
  <svg class="abs ornament" style="top:2040px" width="1200" height="80" viewBox="0 0 1200 80">
    <path d="M0 13 H500 C555 13 585 35 600 63 C615 35 645 13 700 13 H1200" fill="none" stroke="#e9a63c" stroke-width="18"/>
  </svg>
  <div class="abs footer-url">www.corkandlantern.com</div>
  <div class="abs footer-brand">
    <div class="brand-name"><span class="brand-dot"></span><span>Cork And<br>Lantern</span></div>
  </div>

</div>
</body>
</html>
```